Car rental website design for a UAE car rental company

This project is about creating a new website design for a car rental company located in Dubai (United Arab Emirates), I opened the same project a few months ago but I didn't receive a lot of appealing entries so I closed it but this time I am marking the project as guaranteed to avoid such situation again, if you have already provided a design before then please re-submit again on this project so that it is considered while reviewing all the designs

A few important things:

1- We need a simple non-complex design
2- The final deliverable would be 2 screens (PSD, JPEG ... etc), the first screen is for the home page and the second screen is for an internal page
3- The home page must have a section that end users can use to rent a car online directly from the home page instead of going into some inner pages
4- The current website is very old and not very appealing so avoid creating a similar design (www.quarvin-drive.example)
5- The name is Quarvin but the company rents normal cars (no Limousin cars will be rented) so avoid adding any fancy cars in the images/graphics used in the design, just normal end users cars
6- The expected pages would be: home, About us, Our team, Strategy, Contact us and links to social media pages
7- The attachments include the company's logo and some screens from other car rental companies that provide online rentals/payments

If you have any questions please feel free to ask and please note that we will need the designs urgently

Thanks

Target Market(s)

Dubai - United Arab Emirates

Industry/Entity Type

It Company

Number of Pages Required

2 page

Font styles to use
Sans Serif

Requirements
Must have
• Check the project details
Nice to have
Should not have

```html
<!DOCTYPE html>
<html lang="en">
<head>
<meta charset="utf-8">
<title>Quarvin – Rent A Car</title>
<link href="https://fonts.googleapis.com/css2?family=Open+Sans:wght@400;600;700&display=swap" rel="stylesheet">
<style>
:root{
  --crimson:#a4053c;
  --crimson-dark:#8a0232;
  --ink:#2b2b2b;
  --charcoal:#232425;
  --panel:#ececec;
  --line:#cfcfcf;
  --white:#ffffff;
  --pink:#d8144e;
}
*{box-sizing:border-box;margin:0;padding:0}
html,body{width:1200px;height:2308px;overflow:hidden}
body{font-family:"Open Sans",Arial,sans-serif;color:var(--ink);background:var(--white);position:relative}
.abs{position:absolute}

/* header */
.site-header{position:absolute;top:0;left:0;width:1200px;height:68px;background:var(--white)}
.brand{position:absolute;left:98px;top:14px;display:flex;align-items:center;gap:10px}
.brand-mark{width:36px;height:36px;border:3px solid var(--crimson)}
.brand-name{font-size:28px;font-weight:600;color:var(--crimson);line-height:1}
.main-nav{position:absolute;right:98px;top:19px;display:flex;gap:6px}
.main-nav a{font-size:12px;color:#333;text-decoration:none;padding:5px 13px;border:1px solid transparent;text-transform:uppercase}
.main-nav a.active{border-color:var(--crimson)}

/* hero */
.hero{position:absolute;top:68px;left:0;width:1200px;height:547px;background:radial-gradient(ellipse at 70% 40%,#6d6d6d 0%,#3a3a3a 45%,#1c1c1c 100%)}
.hero-photo{position:absolute;left:560px;top:190px;width:520px;height:280px;background:radial-gradient(ellipse at 50% 55%,#2a2a2a 0%,#141414 60%,rgba(20,20,20,0) 75%)}
.booking{position:absolute;left:98px;top:64px;width:404px;height:406px;background:var(--panel);padding:35px 34px}
.booking::after{content:"";position:absolute;right:-22px;top:0;border-left:22px solid var(--panel);border-bottom:22px solid transparent}
.field{height:40px;background:#f1f1f1;border:1px solid #bdbdbd;font-size:15px;color:#333;display:flex;align-items:center;padding:0 18px;position:relative}
.caret{position:absolute;right:14px;top:15px;width:0;height:0;border-left:4px solid transparent;border-right:4px solid transparent;border-top:6px solid #888}
.row{display:flex;margin-top:12px}
.tag{width:100px;height:40px;background:var(--crimson);color:var(--white);font-size:15px;display:flex;align-items:center;justify-content:center;flex:none}
.row .field{flex:1}
.note{font-size:11.5px;color:#333;margin:14px 0 14px}
.time{width:100px;margin-left:6px;flex:none!important}
.btn-reserve{margin-top:22px;height:40px;background:linear-gradient(#b00741,var(--crimson-dark));color:var(--white);font-size:14px;display:flex;align-items:center;justify-content:center;text-transform:uppercase}
.hero-title{position:absolute;left:538px;top:123px;color:var(--white);text-transform:uppercase;line-height:1.15}
.hero-title b{display:block;font-size:33px;font-weight:700}
.hero-title span{display:block;font-size:33px;font-weight:400}
.dots{position:absolute;display:flex;gap:6px}
.dots i{width:11px;height:11px;border-radius:50%;background:var(--white);display:block}
.dots i.on{background:var(--crimson)}
.social{position:absolute;right:0;top:209px;width:48px}
.social i{display:block;height:48px;position:relative}
.social i::after{content:"";position:absolute;left:18px;top:18px;width:12px;height:12px;border-radius:50%;background:rgba(255,255,255,.85)}

/* welcome */
.welcome{position:absolute;top:615px;left:0;width:1200px;height:226px;background:linear-gradient(var(--crimson),var(--crimson-dark));text-align:center;color:var(--white)}
.welcome h1{font-size:30px;font-weight:700;margin-top:28px;text-transform:uppercase}
.welcome p{width:980px;margin:14px auto 0;font-size:12.5px;line-height:1.6}
.btn-dark{display:inline-flex;align-items:center;justify-content:center;width:146px;height:48px;background:var(--charcoal);color:var(--white);font-size:15px;margin-top:24px;text-transform:uppercase}

/* featured */
.section-title{position:absolute;left:0;width:1200px;text-align:center;font-size:30px;font-weight:700;text-transform:uppercase}
.car-card{position:absolute;top:950px;width:231px;height:323px;border:1px solid #dcdcdc;background:var(--white);padding:8px}
.car-photo{height:214px}
.car-name{color:var(--pink);font-size:12.5px;margin:20px 8px 0;line-height:1.35;height:36px}
.price{display:flex;align-items:center;gap:10px;margin:10px 8px 0;font-size:17px}
.price .old{background:var(--pink);color:var(--white);padding:1px 7px}

/* testimonials */
.testimonials{position:absolute;top:1335px;left:0;width:1200px;height:411px;background:var(--charcoal)}
.testimonials .section-title{color:var(--white);top:40px}
.quote{position:absolute;width:490px;display:flex;gap:22px;color:var(--white)}
.avatar{width:86px;height:86px;flex:none}
.quote h3{font-size:17px;font-weight:700;margin-top:2px}
.quote p{font-size:11.5px;line-height:1.85;color:#b8b8b8;margin-top:8px}
.quote p em{font-style:normal;color:var(--pink)}

/* newsletter */
.newsletter{position:absolute;top:1746px;left:0;width:1200px;height:89px}
.newsletter h2{position:absolute;left:98px;top:29px;font-size:25px;color:var(--crimson);font-weight:700;text-transform:uppercase}
.input{position:absolute;height:35px;border:1px solid #a9a9a9;font-size:15px;padding:7px 12px;color:#333}
.btn-submit{position:absolute;left:954px;top:28px;width:149px;height:35px;background:var(--crimson);color:var(--white);font-size:15px;display:flex;align-items:center;justify-content:center}

/* footer */
.site-footer{position:absolute;top:1835px;left:0;width:1200px;height:412px;background:var(--crimson);color:var(--white)}
.col{position:absolute;top:60px;width:232px}
.col h4{font-size:25px;font-weight:400;text-transform:uppercase;margin-bottom:26px}
.address{font-size:12px;line-height:2}
.links li{list-style:none;font-size:13px;padding:7px 0 8px;border-bottom:1px solid rgba(255,255,255,.2)}
.links li::before{content:"» ";font-size:11px}
.tweet{font-size:13px;line-height:1.6;margin-bottom:20px}
.fbox{height:37px;border:1px solid rgba(255,255,255,.75);font-size:13px;padding:8px 14px;margin-bottom:8px}
.fbox.msg{height:82px}
.btn-send{width:110px;height:37px;background:var(--charcoal);font-size:12px;display:flex;align-items:center;justify-content:center;margin-top:14px;text-transform:uppercase}
.bottom-bar{position:absolute;top:2247px;left:0;width:1200px;height:61px;background:var(--charcoal);color:var(--white);font-size:12.5px}
.bottom-bar span{position:absolute;left:98px;top:22px}
</style>
</head>
<body>

<header class="site-header">
  <div class="brand"><span class="brand-mark"></span><span class="brand-name">Quarvin</span></div>
  <nav class="main-nav">
    <a class="active">Home</a><a>About Us</a><a>Our Team</a><a>Strategy</a><a>Contact Us</a>
  </nav>
</header>

<section class="hero">
  <div class="hero-photo" role="img" aria-label="Black saloon car on a blurred city background"></div>
  <form class="booking">
    <div class="field">Select Your Car Type<span class="caret"></span></div>
    <div class="row"><span class="tag">Pick-up</span><div class="field">Enter a City or Airport</div></div>
    <p class="note">Need a different drop-off location?</p>
    <div class="row"><span class="tag">Pick-up</span><div class="field">mm/dd/yyyy<span class="caret"></span></div><div class="field time">12:00 AM<span class="caret"></span></div></div>
    <div class="row"><span class="tag">Drop-off</span><div class="field">mm/dd/yyyy<span class="caret"></span></div><div class="field time">12:00 AM<span class="caret"></span></div></div>
    <div class="btn-reserve">Continue Car Reservation</div>
  </form>
  <h2 class="hero-title"><b>Luxury Car from $28 Day</b><span>Treat Yourself in USA</span></h2>
  <div class="dots" style="left:557px;top:502px"><i></i><i></i><i class="on"></i><i></i><i></i></div>
  <div class="social" aria-label="Social links">
    <i style="background:#3b5998"></i><i style="background:#1fb6e8"></i><i style="background:#dc4a38"></i><i style="background:#b01c2a"></i><i style="background:#27d3b6"></i><i style="background:#f26522"></i>
  </div>
</section>

<section class="welcome">
  <h1>Welcome to Quarvin</h1>
  <p>Lorem Ipsum is simply dummy text of the printing and typesetting industry. Lorem Ipsum has been the industry's standard dummy text ever since the 1500s, when an unknown printer took a galley of type and scrambled it to make a type specimen book.</p>
  <span class="btn-dark">Read More</span>
</section>

<h2 class="section-title" style="top:880px">Featured Cars</h2>
<article class="car-card" style="left:100px">
  <div class="car-photo" role="img" aria-label="White sports car on a road" style="background:linear-gradient(#8a8f92,#d6d6d6 55%,#5d5d5d)"></div>
  <p class="car-name">Consectetur adipisicing elit</p>
  <div class="price"><span class="old">$25,000</span><span>$23,750</span></div>
</article>
<article class="car-card" style="left:357px">
  <div class="car-photo" role="img" aria-label="Red hatchback by the sea" style="background:linear-gradient(#7fa6c4,#c9482a 55%,#4a4a4a)"></div>
  <p class="car-name">Mollitia quae laboriosam corporis delectus</p>
  <div class="price"><span>$38,999</span></div>
</article>
<article class="car-card" style="left:615px">
  <div class="car-photo" role="img" aria-label="Silver SUV on a dark background" style="background:linear-gradient(#1d1d1d,#9a9a9a 55%,#2a2a2a)"></div>
  <p class="car-name">Non magni autem repellendus</p>
  <div class="price"><span class="old">$70,500</span><span>$64,860</span></div>
</article>
<article class="car-card" style="left:872px">
  <div class="car-photo" role="img" aria-label="Black hatchback on a pale studio background" style="background:linear-gradient(#cfd6dc,#9aa3a8 50%,#2d2d2d 80%,#b9bec2)"></div>
  <p class="car-name">Exercitationem voluptate beatae</p>
  <div class="price"><span class="old">$70,500</span><span>$66,975</span></div>
</article>

<section class="testimonials">
  <h2 class="section-title">Testimonials</h2>
  <div class="quote" style="left:98px;top:117px">
    <div class="avatar" role="img" aria-label="Customer portrait" style="background:linear-gradient(#a9a9a9,#565656)"></div>
    <div><h3>Integer vitae libero</h3><p>Praesent dapibus, neque id cursus faucibus, tortor neque egestas augue, eu vulputate magna eros eu erat. Aliquam erat volutpat. Nam dui mi, tincidunt lorem ipsum dolor <em>» more</em></p></div>
  </div>
  <div class="quote" style="left:612px;top:117px">
    <div class="avatar" role="img" aria-label="Customer portrait" style="background:linear-gradient(#cfcfcf,#6d6a78)"></div>
    <div><h3>Vestibulum commodo</h3><p>Lorem dapibus, neque id cursus faucibus, tortor neque egestas augue, eu vulputate magna eros eu erat. Aliquam erat volutpat. Nam dui mi, tincid-unt quis, accumsan porttitor <em>» more</em></p></div>
  </div>
  <div class="quote" style="left:98px;top:229px">
    <div class="avatar" role="img" aria-label="Customer portrait" style="background:linear-gradient(#d0d0d0,#3c3c3c)"></div>
    <div><h3>Fusce pellentesque</h3><p>Cations t dapibus, neque id cursus faucibus, tortor neque egestas augue, eu vulputate magna eros eu erat. Aliquam erat volutpat. Nam dui mi, tincidunt quis, accumsan porttitor, facilisis luctus, metus <em>» more</em></p></div>
  </div>
  <div class="quote" style="left:612px;top:229px">
    <div class="avatar" role="img" aria-label="Customer portrait" style="background:linear-gradient(#e2e2e2,#5a4a44)"></div>
    <div><h3>Donec quis dui dolor</h3><p>Sumitris dapibus, neque id cursus faucibus, tortor neque egestas augue, eu vulputate magna eros eu erat. Aliquam erat volutpat. Nam dui mi, tincid-unt quis, accumsan porttitor, facilisis luctus, metus <em>» more</em></p></div>
  </div>
  <div class="dots" style="left:566px;top:356px"><i></i><i class="on"></i><i></i><i></i></div>
</section>

<section class="newsletter">
  <h2>Signup for Newsletter</h2>
  <div class="input" style="left:441px;top:28px;width:233px">Name</div>
  <div class="input" style="left:697px;top:28px;width:233px">Email</div>
  <div class="btn-submit">Submit</div>
</section>

<footer class="site-footer">
  <div class="col" style="left:98px">
    <h4>Contact</h4>
    <p class="address">Quarvin<br><br>(Melbourne Office / Head Office)<br>Level 4, Suite 402 / 18 Harbour Lane,<br>Corvale, VIC 3990<br>Phone: (03) 5550 142<br>(Brisbane Office)<br>Shop 3/210 Ridgeway Road,<br>Fernmoor, QLD 4990<br>(07) 5550 3187</p>
  </div>
  <div class="col" style="left:355px">
    <h4>Quick Links</h4>
    <ul class="links"><li>Lorem ipsum dolor sit</li><li>Amet consectetur</li><li>Praesent vel sem id</li><li>Curabitur hendrerit est</li><li>Aliquam eget erat nec sapien</li><li>Cras id augue nunc</li><li>Sed a nulla urna</li></ul>
  </div>
  <div class="col" style="left:611px">
    <h4>Latest Tweets</h4>
    <p class="tweet">@namehere justoid nonummy laoreet phasellent penatoque in antesque pellus elis eget tincidunt. Nequatdui laorem justo a non tellus laoreml vitae doloreet 1 day ago</p>
    <p class="tweet">@namehere justoid nonummy laoreet phasellent penatoque in antesque pellus elis eget tincidunt. Nequatdui laorem justo a non tellus laoreml vitae doloreet 1 day ago</p>
  </div>
  <div class="col" style="left:869px">
    <h4>Contact Us</h4>
    <div class="fbox">Full Name</div>
    <div class="fbox">Email Address</div>
    <div class="fbox">Subject</div>
    <div class="fbox msg">Message</div>
    <div class="btn-send">Submit</div>
  </div>
</footer>

<div class="bottom-bar"><span>Copyright © 2015 quarvin-drive.example - All Rights Reserved</span></div>

</body>
</html>
```